Asphalt Paving Specialists Business Cards

Our company is KORVEN ASPHALT. We need a business cards two of our asphalt paving team members. We're asphalt specialists.
I need two made up please. The details on the front of the each business card i would like please is as follows.
Address is 87 Tindale Ave, Clontarf, QLD, 4019.

Company Director
Gregory Pellinham
greg@korven-example.com.au
04 87 659 042
www.korven-example.com.au

Supervisor
Lewis Marchetti
lewis@korven-example.com.au
0468 701 385
www.korven-example.com.au

We do all aspects of Asphalt Paving. Specific Services include - Driveways, Carparks & sub-divisions. All Roads. Repairs and Maintenance.

We provide free quotes!

I dont have a certain way i want them to look so im open to all designs :)

** I have uploaded our logo for the KORVEN ASPHALT. HOWEVER, CAN YOU PLEASE GET RID OF THE ( PTY LTD )

Thank you
Carina Holt
KORVEN ASPHALT

Target Market(s)

Home owners and Business Owners

Contact Information for Business Card

Asphalt Paving Specialists. All aspects of Asphalt. Residential, Commercial & Industrial. Based in Brisbane.

Font styles to use
Sans Serif

Colors

Designer to choose colors to be used in the design.

Requirements
Nice to have
• maybe an image of a driveway? or Asphalt?

```html
<!DOCTYPE html>
<html lang="en">
<head>
<meta charset="utf-8">
<title>Korven Asphalt – Business Card</title>
<link rel="stylesheet" href="https://fonts.googleapis.com/css2?family=Archivo:wdth,wght@62..125,300..900&display=swap">
<style>
  :root {
    --asphalt-dark: #2c2b2c;
    --asphalt-mid: #3c3b3c;
    --asphalt-light: #4a4949;
    --ink-white: #efefef;
    --ink-soft: #e2e2e2;
  }
  html, body {
    margin: 0;
    padding: 0;
    width: 1200px;
    height: 667px;
    overflow: hidden;
    background: var(--asphalt-dark);
  }
  .card {
    position: relative;
    width: 1200px;
    height: 667px;
    overflow: hidden;
    font-family: "Archivo", Arial, sans-serif;
    color: var(--ink-white);
  }
  .asphalt-surface {
    position: absolute;
    inset: 0;
    background:
      radial-gradient(ellipse at 30% 25%, var(--asphalt-light) 0%, transparent 60%),
      radial-gradient(ellipse at 80% 85%, var(--asphalt-mid) 0%, transparent 55%),
      linear-gradient(160deg, var(--asphalt-mid) 0%, var(--asphalt-dark) 100%);
  }
  .role {
    position: absolute;
    left: 77px;
    top: 88px;
    margin: 0;
    font-size: 38px;
    font-weight: 400;
    letter-spacing: 1.5px;
    color: var(--ink-soft);
    line-height: 1;
  }
  .name {
    position: absolute;
    left: 77px;
    top: 152px;
    margin: 0;
    font-size: 106px;
    font-weight: 850;
    font-stretch: 88%;
    letter-spacing: 0.5px;
    line-height: 1;
    white-space: nowrap;
    color: var(--ink-white);
  }
  .contact {
    position: absolute;
    right: 85px;
    top: 375px;
    text-align: right;
  }
  .email {
    display: block;
    font-size: 37px;
    font-weight: 800;
    letter-spacing: 2.5px;
    line-height: 1;
    color: var(--ink-white);
  }
  .phone {
    display: flex;
    justify-content: flex-end;
    align-items: center;
    gap: 12px;
    margin-top: 60px;
    font-size: 44px;
    font-weight: 300;
    letter-spacing: 8px;
    line-height: 1;
    margin-right: -8px;
    color: var(--ink-white);
  }
  .phone-icon {
    width: 46px;
    height: 46px;
    flex: none;
  }
  .web {
    display: block;
    margin-top: 14px;
    font-size: 40px;
    font-weight: 400;
    letter-spacing: 1.5px;
    line-height: 1;
    color: var(--ink-soft);
  }
</style>
</head>
<body>
  <main class="card">
    <div class="asphalt-surface" role="img" aria-label="Close-up texture of dark grey asphalt paving"></div>

    <p class="role">Company Director</p>
    <h1 class="name">Gregory Pellinham</h1>

    <div class="contact">
      <span class="email">greg@korven-example.com.au</span>
      <span class="phone">
        <svg class="phone-icon" viewBox="0 0 46 46" aria-hidden="true">
          <circle cx="23" cy="23" r="21" fill="none" stroke="#efefef" stroke-width="2.5"/>
          <path d="M16 13c1.5-1 3-0.6 3.6 0.8l1.5 3.3c0.5 1.1 0.2 2-0.8 2.7l-1.4 1c0.9 2.4 2.8 4.5 5.2 5.6l1-1.4c0.7-1 1.7-1.3 2.8-0.8l3.2 1.5c1.4 0.6 1.7 2.2 0.8 3.6-1.3 2-3.4 2.8-5.6 2-6.1-2.2-10.4-6.6-12.4-12.6-0.7-2.2 0.2-4.4 2.1-5.7z" fill="#efefef"/>
        </svg>
        04 87 659 042
      </span>
      <span class="web">www.korven-example.com.au</span>
    </div>
  </main>
</body>
</html>
```